Redesign of Medical App for Patients

• The Designer’s task is to provide a new fully-responsive design for our apps, and then code it using only basic html and CSS.
• Your design will be incorporated into our existing REACT native app.

Target Market(s)

Medical Patients

Industry/Entity Type

Medical

Coding

Coded - Design and coding required

Number of Pages Required

5+ page

Requirements
Must have
• Short list candidates will receive detailed briefing
Nice to have
• detailed briefing contains some of our ideas.

```html
<!DOCTYPE html>
<html lang="en">
<head>
<meta charset="utf-8">
<title>CareLink – Patient App Screens</title>
<link href="https://fonts.googleapis.com/css2?family=Inter:wght@400;500;600;700&display=swap" rel="stylesheet">
<style>
:root{
  --stage:#393939;
  --paper:#ffffff;
  --ink:#1b1b1b;
  --muted:#8b8b8b;
  --line:#cfcfcf;
  --blue:#1a85c6;
  --blue-soft:#d8eef9;
  --teal:#17a9b5;
  --mint:#37d6a0;
  --success-bg:#dcf3ef;
  --grey-btn:#5c5c5c;
}
*{box-sizing:border-box;margin:0;padding:0}
html,body{width:1200px;height:710px;overflow:hidden}
body{background:var(--stage);font-family:"Inter",sans-serif;color:var(--ink);position:relative}
.screen{position:absolute;width:149px;background:var(--paper);border-radius:14px;overflow:hidden}
.row-top{top:22px;height:323px}
.row-bottom{top:367px;height:321px}
.abs{position:absolute}
.center{left:0;right:0;text-align:center}
.btn{position:absolute;background:var(--blue);color:#fff;border-radius:4px;font-size:7px;font-weight:500;display:flex;align-items:center;justify-content:center;gap:3px}
.muted{color:var(--muted)}
.art{position:absolute;border-radius:8px}
/* top bar */
.topbar .ico{position:absolute;width:12px;height:12px;stroke:var(--ink);fill:none;stroke-width:1.6}
.dot{position:absolute;width:4px;height:4px;border-radius:50%;background:var(--mint)}
/* tab bar */
.tabbar{position:absolute;left:0;right:0;bottom:0;height:34px;display:flex;justify-content:space-around;padding:0 8px;align-items:center;background:linear-gradient(#f7f7f7,#fff)}
.tab{display:flex;flex-direction:column;align-items:center;gap:2px;font-size:4.6px;color:#333;width:30px}
.tab svg{width:12px;height:12px;fill:none;stroke:currentColor;stroke-width:1.4}
.tab.is-active{color:var(--blue)}
/* form */
.field-label{position:absolute;left:10px;font-size:7px;color:var(--muted)}
.field-value{position:absolute;left:10px;font-size:7.4px;color:var(--ink)}
.field-line{position:absolute;left:10px;width:130px;height:1px;background:var(--line)}
/* radios */
.radio{position:absolute;width:10px;height:10px;border:1px solid #b8b8b8;border-radius:50%}
.radio.on{background:var(--blue);border-color:var(--blue)}
.radio.on::after{content:"";position:absolute;left:3px;top:1.3px;width:2.4px;height:4.4px;border:solid #fff;border-width:0 1.2px 1.2px 0;transform:rotate(45deg)}
.opt{position:absolute;font-size:6.2px;color:#333;line-height:1.35}
.card{position:absolute;background:#fff;border-radius:6px;box-shadow:0 2px 8px rgba(0,0,0,.08)}
</style>
</head>
<body>
<svg width="0" height="0" style="position:absolute">
  <defs>
    <symbol id="i-bell" viewBox="0 0 24 24"><path d="M6 17V11a6 6 0 0 1 12 0v6l2 2H4z"/><path d="M10 21h4"/></symbol>
    <symbol id="i-user" viewBox="0 0 24 24"><circle cx="12" cy="12" r="10"/><circle cx="12" cy="10" r="3.5"/><path d="M5.5 19c2-3 4-4 6.5-4s4.5 1 6.5 4"/></symbol>
    <symbol id="i-back" viewBox="0 0 24 24"><path d="M21 12H4M10 5l-7 7 7 7"/></symbol>
    <symbol id="i-menu" viewBox="0 0 24 24"><path d="M3 6h16M3 12h12M3 18h16"/></symbol>
    <symbol id="i-home" viewBox="0 0 24 24"><path d="M4 10l8-6 8 6v10H4z"/><path d="M10 20v-6h4v6"/></symbol>
    <symbol id="i-aidoc" viewBox="0 0 24 24"><rect x="5" y="4" width="14" height="17" rx="2"/><path d="M9 3h6v3H9zM7 14h3l2-4 2 6 1-2h2"/></symbol>
    <symbol id="i-community" viewBox="0 0 24 24"><circle cx="12" cy="6" r="2.5"/><circle cx="5.5" cy="9" r="2"/><circle cx="18.5" cy="9" r="2"/><path d="M8 20v-8h8v8M3 20v-6h3M21 20v-6h-3"/></symbol>
    <symbol id="i-doctors" viewBox="0 0 24 24"><path d="M5 3h10v18l-5-4-5 4z"/><circle cx="18" cy="5" r="3"/></symbol>
  </defs>
</svg>

<!-- ========== ROW 1 ========== -->

<!-- Welcome -->
<section class="screen row-top" style="left:37px">
  <div class="art" style="left:30px;top:45px;width:93px;height:103px;border-radius:50%;background:radial-gradient(circle,#e4f1fa,#ffffff 75%)" role="img" aria-label="Illustration of a friendly doctor wearing a mask and stethoscope"></div>
  <h1 class="abs center" style="top:166px;font-size:14px;font-weight:700">Your Online Doctor</h1>
  <p class="abs muted" style="left:12px;right:12px;top:190px;font-size:8px;line-height:1.2;text-align:center">Welcome to CareLink. We help you to connect with doctors from all over the nation</p>
  <a class="btn" style="left:36px;top:229px;width:78px;height:26px;font-size:8px">Get Started
    <svg width="7" height="7" viewBox="0 0 24 24" fill="none" stroke="#fff" stroke-width="3"><path d="M9 5l7 7-7 7"/></svg></a>
</section>

<!-- Sign up -->
<section class="screen row-top" style="left:200px">
  <h2 class="abs" style="left:10px;top:19px;font-size:14px;font-weight:700">Sign Up Now</h2>
  <p class="abs muted" style="left:10px;top:42px;font-size:8px;line-height:1.15;width:110px">Fill up the details to create an Account</p>
  <span class="field-label" style="top:78px">Name</span><span class="field-value" style="top:90px">John Doe</span><span class="field-line" style="top:101px"></span>
  <span class="field-label" style="top:110px">Email</span><span class="field-value" style="top:122px">johndoe@mailbox.test</span><span class="field-line" style="top:133px"></span>
  <span class="field-label" style="top:142px">Number</span><span class="field-value" style="top:154px">(+)0001234567890</span><span class="field-line" style="top:165px"></span>
  <span class="field-label" style="top:174px">Password</span><span class="field-value" style="top:184px;letter-spacing:1px;font-size:8px">●●●●●●</span><span class="field-line" style="top:197px"></span>
  <a class="btn" style="left:34px;top:209px;width:82px;height:26px">Create Account</a>
  <p class="abs center muted" style="top:246px;font-size:7.4px;color:#666">Already have an account? <u>Log in</u></p>
  <p class="abs center muted" style="top:264px;font-size:6.5px;color:#aaa">Or sign up with socials</p>
  <span class="abs" style="left:34px;top:281px;width:23px;height:23px;border-radius:50%;background:#fff;box-shadow:0 2px 6px rgba(0,0,0,.12);font-size:4.6px;display:flex;align-items:center;justify-content:center;color:#555">Orbit</span>
  <span class="abs" style="left:63px;top:281px;width:23px;height:23px;border-radius:50%;background:#3b5bab;font-size:4.6px;display:flex;align-items:center;justify-content:center;color:#fff">Frendly</span>
  <span class="abs" style="left:92px;top:281px;width:23px;height:23px;border-radius:50%;background:#2aa2ef;font-size:4.6px;display:flex;align-items:center;justify-content:center;color:#fff">Chirper</span>
</section>

<!-- Role -->
<section class="screen row-top" style="left:363px">
  <span class="abs" style="left:9px;top:24px;font-size:8.5px;display:flex;align-items:center;gap:3px">
    <svg width="8" height="8" viewBox="0 0 24 24" fill="none" stroke="#1b1b1b" stroke-width="2.6"><path d="M15 5l-7 7 7 7"/></svg>Back</span>
  <h2 class="abs center" style="top:85px;font-size:15px;font-weight:700;line-height:1.05">What describes<br>you best?</h2>
  <div class="card" style="left:10px;top:131px;width:61px;height:60px;border:1.2px solid var(--blue)">
    <div class="art" style="left:18px;top:8px;width:25px;height:28px;background:linear-gradient(#f0c9a5,#4fc4c0)" role="img" aria-label="Patient avatar"></div>
    <span class="abs center" style="top:44px;font-size:7.2px">I'm a Patient</span>
  </div>
  <div class="card" style="left:79px;top:131px;width:61px;height:60px">
    <div class="art" style="left:18px;top:8px;width:25px;height:28px;background:linear-gradient(#f0c9a5,#cfe6f2)" role="img" aria-label="Doctor avatar"></div>
    <span class="abs center" style="top:44px;font-size:7.2px">I'm a Doctor</span>
  </div>
  <a class="btn" style="left:37px;top:208px;width:75px;height:25px">Let's Proceed
    <svg width="7" height="7" viewBox="0 0 24 24" fill="none" stroke="#fff" stroke-width="2.6"><path d="M4 12h15M13 6l6 6-6 6"/></svg></a>
  <div class="abs center" style="top:288px;display:flex;justify-content:center;align-items:center;gap:4px">
    <span style="width:14px;height:14px;border-radius:50%;background:var(--blue)"></span>
    <span style="font-size:9.5px;font-weight:600;color:#2d3b55">CareLink</span>
  </div>
</section>

<!-- Home -->
<section class="screen row-top" style="left:525px">
  <div class="topbar">
    <svg class="ico" style="left:9px;top:20px"><use href="#i-menu"/></svg>
    <svg class="ico" style="left:106px;top:20px"><use href="#i-bell"/></svg><span class="dot" style="left:115px;top:19px"></span>
    <svg class="ico" style="left:127px;top:20px"><use href="#i-user"/></svg>
  </div>
  <p class="abs" style="left:10px;top:44px;font-size:8px;color:#555">Hey Nora,</p>
  <h2 class="abs" style="left:10px;top:55px;font-size:12.5px;font-weight:700;line-height:1">How are you<br>feeling?</h2>
  <div class="art" style="left:10px;top:87px;width:130px;height:117px;background:linear-gradient(120deg,#d7eef8,#c2e4f4)">
    <div class="art" style="left:80px;top:4px;width:50px;height:113px;border-radius:20px 0 8px 0;background:linear-gradient(#f2cda9,#3ec9bf)" role="img" aria-label="Illustration of a masked doctor"></div>
    <p class="abs" style="left:7px;top:26px;font-size:10.5px;font-weight:600;line-height:1.05">Take a health<br>checkup</p>
    <p class="abs muted" style="left:7px;top:57px;width:75px;font-size:6.5px;line-height:1.4">Our Ai Doc analyzes your health related answers and then calculates the possible diseases</p>
  </div>
  <div class="art" style="left:10px;top:210px;width:62px;height:63px;background:linear-gradient(#d3e9f6,#9cc8e3)" role="img" aria-label="Photo of a smiling doctor"></div>
  <div class="art" style="left:78px;top:210px;width:62px;height:63px;background:linear-gradient(#d3e9f6,#4e7fa6)" role="img" aria-label="Photo of a group of volunteers"></div>
  <span class="abs" style="left:10px;width:62px;top:279px;font-size:6.8px;color:#666;text-align:center">Book a Doctor</span>
  <span class="abs" style="left:78px;width:62px;top:279px;font-size:6.8px;color:#666;text-align:center">Join Community</span>
  <nav class="tabbar">
    <a class="tab is-active"><svg><use href="#i-home"/></svg>Home</a>
    <a class="tab"><svg><use href="#i-aidoc"/></svg>Ai Doc</a>
    <a class="tab"><svg><use href="#i-community"/></svg>Community</a>
    <a class="tab"><svg><use href="#i-doctors"/></svg>Doctors</a>
  </nav>
</section>

<!-- Doctor profile -->
<section class="screen row-top" style="left:686px">
  <div class="topbar">
    <svg class="ico" style="left:9px;top:20px"><use href="#i-menu"/></svg>
    <svg class="ico" style="left:106px;top:20px"><use href="#i-bell"/></svg><span class="dot" style="left:115px;top:19px"></span>
    <svg class="ico" style="left:127px;top:20px"><use href="#i-user"/></svg>
  </div>
  <div class="art" style="left:9px;top:49px;width:57px;height:77px;background:linear-gradient(#d6ecf8,#ffffff)" role="img" aria-label="Portrait photo of the cardiologist"></div>
  <p class="abs muted" style="left:74px;top:53px;font-size:6.8px">&#9679; Top Doctor</p>
  <h3 class="abs" style="left:74px;top:71px;font-size:10px;font-weight:600">Dr. Arlen</h3>
  <p class="abs muted" style="left:74px;top:84px;font-size:7.2px">Cardiologist</p>
  <p class="abs muted" style="left:74px;top:104px;font-size:6.8px">&#9733; 4.6 out of 5</p>
  <p class="abs muted" style="left:74px;top:116px;font-size:6.8px">&#9679; 130+ Patients</p>
  <a class="btn" style="left:9px;top:137px;width:106px;height:24px">Book Appointment</a>
  <a class="btn" style="left:119px;top:137px;width:21px;height:21px">
    <svg width="9" height="9" viewBox="0 0 24 24" fill="none" stroke="#fff" stroke-width="2"><rect x="3" y="5" width="18" height="14" rx="1"/><path d="M3 6l9 7 9-7"/></svg></a>
  <div class="card" style="left:9px;top:172px;width:131px;height:108px">
    <h4 class="abs" style="left:7px;top:8px;font-size:8px;font-weight:500">Biography</h4>
    <p class="abs muted" style="left:7px;top:24px;width:120px;font-size:6.2px;line-height:1.45">Dr. Tomas Vey was born in Brookhaven, Marlow County and is a graduate of Westbridge College. He obtained his medical degree at Northgate Medical School. <span style="color:var(--blue)">Read More</span></p>
    <h4 class="abs" style="left:7px;top:75px;font-size:8px;font-weight:500">Location</h4>
    <p class="abs muted" style="left:7px;top:89px;font-size:6.5px">Riverton, Eastland</p>
  </div>
  <nav class="tabbar">
    <a class="tab"><svg><use href="#i-home"/></svg>Home</a>
    <a class="tab"><svg><use href="#i-aidoc"/></svg>Ai Doc</a>
    <a class="tab"><svg><use href="#i-community"/></svg>Community</a>
    <a class="tab is-active"><svg><use href="#i-doctors"/></svg>Doctors</a>
  </nav>
</section>

<!-- Discover -->
<section class="screen row-top" style="left:847px">
  <div class="topbar">
    <svg class="ico" style="left:9px;top:20px"><use href="#i-back"/></svg>
    <svg class="ico" style="left:106px;top:20px"><use href="#i-bell"/></svg><span class="dot" style="left:115px;top:19px"></span>
    <svg class="ico" style="left:127px;top:20px"><use href="#i-user"/></svg>
  </div>
  <h2 class="abs" style="left:10px;top:47px;font-size:13px;font-weight:700">Discover</h2>
  <div class="card" style="left:10px;top:70px;width:129px;height:24px;display:flex;align-items:center;justify-content:space-between;padding:0 8px">
    <span style="font-size:6.5px;color:#b0b0b0">Search "Medical Problems"</span>
    <svg width="8" height="8" viewBox="0 0 24 24" fill="none" stroke="#333" stroke-width="2.4"><circle cx="14" cy="10" r="6"/><path d="M9.5 14.5L4 20"/></svg>
  </div>
  <span class="abs" style="left:10px;top:100px;font-size:6.8px;color:#555">&#9663; Filter</span>
  <span class="abs" style="right:10px;top:100px;font-size:6.5px;color:var(--blue)">See All</span>
  <article class="card" style="left:10px;top:115px;width:128px;height:79px">
    <span class="abs" style="left:6px;top:5px;width:14px;height:14px;border-radius:50%;background:#c0513d"></span>
    <b class="abs" style="left:25px;top:8px;font-size:7.2px;font-weight:500">Arin Kole</b>
    <p class="abs muted" style="left:6px;top:27px;width:114px;font-size:6.4px;line-height:1.4">I can not sleep at night properly. Does that mean I have insomnia? Can someone please give me advices.</p>
    <p class="abs" style="left:6px;top:67px;font-size:6.2px;color:#555">👍 80 &nbsp; 👎 2 &nbsp; ▭ 68</p>
  </article>
  <article class="card" style="left:10px;top:202px;width:128px;height:79px">
    <span class="abs" style="left:6px;top:5px;width:14px;height:14px;border-radius:50%;background:#6b5848"></span>
    <b class="abs" style="left:25px;top:8px;font-size:7.2px;font-weight:500">Tamim Rahe</b>
    <p class="abs muted" style="left:6px;top:27px;width:114px;font-size:6.4px;line-height:1.4">What is the best herbal medicine to increase hair growth? Please suggest me some in the comment section.</p>
    <p class="abs" style="left:6px;top:67px;font-size:6.2px;color:#555">👍 224 &nbsp; 👎 0 &nbsp; ▭ 68</p>
  </article>
  <span class="abs" style="left:117px;top:256px;width:26px;height:26px;border-radius:50%;background:var(--blue);color:#fff;font-size:18px;line-height:24px;text-align:center">+</span>
  <nav class="tabbar">
    <a class="tab"><svg><use href="#i-home"/></svg>Home</a>
    <a class="tab"><svg><use href="#i-aidoc"/></svg>Ai Doc</a>
    <a class="tab is-active"><svg><use href="#i-community"/></svg>Community</a>
    <a class="tab"><svg><use href="#i-doctors"/></svg>Doctors</a>
  </nav>
</section>

<!-- ========== ROW 2 ========== -->

<!-- Hello -->
<section class="screen row-bottom" style="left:37px">
  <div class="topbar">
    <svg class="ico" style="left:9px;top:19px"><use href="#i-back"/></svg>
    <svg class="ico" style="left:106px;top:19px"><use href="#i-bell"/></svg><span class="dot" style="left:115px;top:18px"></span>
    <svg class="ico" style="left:127px;top:19px"><use href="#i-user"/></svg>
  </div>
  <div class="art" style="left:27px;top:64px;width:93px;height:86px;border-radius:45% 50% 40% 50%;background:linear-gradient(135deg,#3fc9c6,#1a82b8)" role="img" aria-label="Illustration of three medical workers in scrubs"></div>
  <h2 class="abs center" style="top:160px;font-size:12px;font-weight:500;color:#333">Hello!</h2>
  <p class="abs muted" style="left:10px;right:10px;top:184px;font-size:6.4px;line-height:1.4;text-align:center">You're about to use a short (3 min), safe and anonymous health checkup. Your answers will be carefully analyzed and you'll learn about your current condition and what do you have to do.</p>
  <a class="btn" style="left:44px;top:235px;width:60px;height:24px">I am Ready</a>
  <nav class="tabbar">
    <a class="tab"><svg><use href="#i-home"/></svg>Home</a>
    <a class="tab is-active"><svg><use href="#i-aidoc"/></svg>Ai Doc</a>
    <a class="tab"><svg><use href="#i-community"/></svg>Community</a>
    <a class="tab"><svg><use href="#i-doctors"/></svg>Doctors</a>
  </nav>
</section>

<!-- Terms -->
<section class="screen row-bottom" style="left:200px">
  <div class="topbar">
    <svg class="ico" style="left:9px;top:19px"><use href="#i-back"/></svg>
    <svg class="ico" style="left:106px;top:19px"><use href="#i-bell"/></svg><span class="dot" style="left:115px;top:18px"></span>
    <svg class="ico" style="left:127px;top:19px"><use href="#i-user"/></svg>
  </div>
  <h2 class="abs" style="left:10px;top:56px;font-size:11.5px;font-weight:500">Terms of Service</h2>
  <p class="abs" style="left:10px;top:80px;width:128px;font-size:6.3px;line-height:1.35;color:#555">Before using the checkup, please read Terms of Service. Remember that:</p>
  <ul class="abs" style="left:17px;top:107px;width:122px;font-size:6.3px;line-height:1.35;color:#555;padding-left:7px">
    <li style="margin-bottom:7px">Checkup is not diagnosis. Checkup is for informational purposes and is not a qualified medical opinion</li>
    <li style="margin-bottom:7px">Do no use in emergencies. In case of health emergency call your local emergency number immediately.</li>
    <li>Your data is safe. Information that you provide is anonymous and not shared with anyone.</li>
  </ul>
  <a class="btn" style="left:9px;top:214px;width:130px;height:25px">I agree to Terms of Service</a>
  <a class="btn" style="left:9px;top:245px;width:130px;height:25px;background:var(--grey-btn)">Decline</a>
  <nav class="tabbar">
    <a class="tab"><svg><use href="#i-home"/></svg>Home</a>
    <a class="tab is-active"><svg><use href="#i-aidoc"/></svg>Ai Doc</a>
    <a class="tab"><svg><use href="#i-community"/></svg>Community</a>
    <a class="tab"><svg><use href="#i-doctors"/></svg>Doctors</a>
  </nav>
</section>

<!-- Plans -->
<section class="screen row-bottom" style="left:363px">
  <div class="topbar">
    <svg class="ico" style="left:9px;top:19px"><use href="#i-back"/></svg>
    <svg class="ico" style="left:106px;top:19px"><use href="#i-bell"/></svg><span class="dot" style="left:115px;top:18px"></span>
    <svg class="ico" style="left:127px;top:19px"><use href="#i-user"/></svg>
  </div>
  <h2 class="abs center" style="top:80px;font-size:10.5px;font-weight:500;line-height:1.05">What are your current<br>plans for dealing with your<br>symptoms?</h2>
  <span class="radio" style="left:13px;top:134px"></span><span class="opt" style="left:30px;top:131px;width:112px">I plan to stay at home and take care of myself.</span>
  <span class="radio on" style="left:13px;top:157px"></span><span class="opt" style="left:30px;top:158px">I plan to see a doctor</span>
  <span class="radio" style="left:13px;top:176px"></span><span class="opt" style="left:30px;top:177px">I plan to visit an emergency room</span>
  <span class="radio" style="left:13px;top:194px"></span><span class="opt" style="left:30px;top:195px">I am confused</span>
  <span class="abs" style="left:34px;top:230px;font-size:7.2px;color:#999">Skip this</span>
  <a class="btn" style="left:72px;top:222px;width:43px;height:23px">Next</a>
  <nav class="tabbar">
    <a class="tab"><svg><use href="#i-home"/></svg>Home</a>
    <a class="tab is-active"><svg><use href="#i-aidoc"/></svg>Ai Doc</a>
    <a class="tab"><svg><use href="#i-community"/></svg>Community</a>
    <a class="tab"><svg><use href="#i-doctors"/></svg>Doctors</a>
  </nav>
</section>

<!-- Checkup for -->
<section class="screen row-bottom" style="left:525px">
  <div class="topbar">
    <svg class="ico" style="left:9px;top:19px"><use href="#i-back"/></svg>
    <svg class="ico" style="left:106px;top:19px"><use href="#i-bell"/></svg><span class="dot" style="left:115px;top:18px"></span>
    <svg class="ico" style="left:127px;top:19px"><use href="#i-user"/></svg>
  </div>
  <h2 class="abs center" style="top:64px;font-size:10.5px;font-weight:500">Whom is the checkup for?</h2>
  <div class="card" style="left:10px;top:95px;width:62px;height:60px;border:1.2px solid var(--blue)">
    <svg class="abs" style="left:22px;top:8px" width="18" height="28" viewBox="0 0 18 28" fill="none" stroke="#555" stroke-width="1.2"><circle cx="9" cy="4" r="3"/><path d="M4 26V10h10v16M7 16v10M11 16v10"/></svg>
    <span class="abs center" style="top:42px;font-size:7.4px">Myself</span>
  </div>
  <div class="card" style="left:77px;top:95px;width:62px;height:60px">
    <svg class="abs" style="left:12px;top:8px" width="38" height="28" viewBox="0 0 38 28" fill="none" stroke="#555" stroke-width="1.2"><circle cx="9" cy="4" r="3"/><path d="M4 26V10h10v16M7 16v10M11 16v10"/><circle cx="29" cy="4" r="3"/><path d="M24 26V10h10v16M27 16v10M31 16v10"/></svg>
    <span class="abs center" style="top:42px;font-size:7.4px">Someone Else</span>
  </div>
  <h2 class="abs center" style="top:175px;font-size:10.5px;font-weight:500">How old are you?</h2>
  <span class="abs" style="left:14px;top:210px;width:120px;height:1.5px;background:#ddd"></span>
  <span class="abs" style="left:10px;top:206px;width:9px;height:9px;border-radius:50%;background:var(--blue);color:#fff;font-size:8px;line-height:8px;text-align:center">−</span>
  <span class="abs" style="left:130px;top:206px;width:9px;height:9px;border-radius:50%;background:var(--blue);color:#fff;font-size:8px;line-height:9px;text-align:center">+</span>
  <span class="abs" style="left:46px;top:200px;width:21px;height:21px;border-radius:50%;border:1.4px solid var(--blue);background:#fff;font-size:9px;line-height:18px;text-align:center">19</span>
  <a class="btn" style="left:10px;top:241px;width:130px;height:25px">Next</a>
  <nav class="tabbar">
    <a class="tab"><svg><use href="#i-home"/></svg>Home</a>
    <a class="tab is-active"><svg><use href="#i-aidoc"/></svg>Ai Doc</a>
    <a class="tab"><svg><use href="#i-community"/></svg>Community</a>
    <a class="tab"><svg><use href="#i-doctors"/></svg>Doctors</a>
  </nav>
</section>

<!-- Review statements -->
<section class="screen row-bottom" style="left:688px">
  <div class="topbar">
    <svg class="ico" style="left:9px;top:19px"><use href="#i-back"/></svg>
    <svg class="ico" style="left:106px;top:19px"><use href="#i-bell"/></svg><span class="dot" style="left:115px;top:18px"></span>
    <svg class="ico" style="left:127px;top:19px"><use href="#i-user"/></svg>
  </div>
  <h2 class="abs center" style="top:54px;font-size:10.2px;font-weight:500;line-height:1.03">Please review all of the<br>statements below to see if<br>they apply to you.</h2>
  <p class="abs center" style="top:101px;font-size:6.2px;color:#555">Select one answer in each row</p>

  <p class="opt" style="left:11px;top:125px">1.&nbsp; Are you overweight?</p>
  <span class="radio" style="left:10px;top:141px"></span><span class="opt" style="left:24px;top:142px">Yes</span>
  <span class="radio on" style="left:51px;top:141px"></span><span class="opt" style="left:65px;top:142px">No</span>
  <span class="radio" style="left:89px;top:141px"></span><span class="opt" style="left:103px;top:142px">Don't Know</span>

  <p class="opt" style="left:11px;top:162px">2. Do you have cholesterol?</p>
  <span class="radio" style="left:10px;top:178px"></span><span class="opt" style="left:24px;top:179px">Yes</span>
  <span class="radio" style="left:51px;top:178px"></span><span class="opt" style="left:65px;top:179px">No</span>
  <span class="radio on" style="left:89px;top:178px"></span><span class="opt" style="left:103px;top:179px">Don't Know</span>

  <p class="opt" style="left:11px;top:199px">3. Do you smoke cigarettes?</p>
  <span class="radio on" style="left:10px;top:215px"></span><span class="opt" style="left:24px;top:216px">Yes</span>
  <span class="radio" style="left:51px;top:215px"></span><span class="opt" style="left:65px;top:216px">No</span>
  <span class="radio" style="left:89px;top:215px"></span><span class="opt" style="left:103px;top:216px">Don't Know</span>

  <a class="btn" style="left:10px;top:241px;width:130px;height:25px">Next</a>
  <nav class="tabbar">
    <a class="tab"><svg><use href="#i-home"/></svg>Home</a>
    <a class="tab is-active"><svg><use href="#i-aidoc"/></svg>Ai Doc</a>
    <a class="tab"><svg><use href="#i-community"/></svg>Community</a>
    <a class="tab"><svg><use href="#i-doctors"/></svg>Doctors</a>
  </nav>
</section>

<!-- Analyzing -->
<section class="screen row-bottom" style="left:851px">
  <div class="topbar">
    <svg class="ico" style="left:9px;top:19px"><use href="#i-back"/></svg>
    <svg class="ico" style="left:106px;top:19px"><use href="#i-bell"/></svg><span class="dot" style="left:115px;top:18px"></span>
    <svg class="ico" style="left:127px;top:19px"><use href="#i-user"/></svg>
  </div>
  <div class="art" style="left:27px;top:59px;width:96px;height:141px;border-radius:48px 48px 6px 6px;background:linear-gradient(#4fd0c8,#1a86bd)" role="img" aria-label="Illustration of a doctor holding a report surrounded by gears"></div>
  <h2 class="abs center" style="top:220px;font-size:11px;font-weight:500">Analyzing your report</h2>
  <p class="abs center" style="top:245px;font-size:6px;color:#555;line-height:1.35;text-transform:uppercase">Ai Doc is processing your<br>reports</p>
  <nav class="tabbar">
    <a class="tab"><svg><use href="#i-home"/></svg>Home</a>
    <a class="tab is-active"><svg><use href="#i-aidoc"/></svg>Ai Doc</a>
    <a class="tab"><svg><use href="#i-community"/></svg>Community</a>
    <a class="tab"><svg><use href="#i-doctors"/></svg>Doctors</a>
  </nav>
</section>

<!-- Success -->
<section class="screen row-bottom" style="left:1013px;background:var(--success-bg)">
  <svg class="abs" style="left:50px;top:115px" width="22" height="22" viewBox="0 0 22 22" fill="none" stroke="#23b24a" stroke-width="2.2" stroke-linecap="round"><path d="M3 18A12 12 0 0 1 18 4"/></svg>
  <h2 class="abs center" style="top:190px;font-size:11px;font-weight:500;line-height:1.1;color:#1a8ac7">Report Analyzed<br>Successfully</h2>
</section>

</body>
</html>
```